Brume d'Orvelle Hand Crafted Candles promotional flyer

Hand Crafted Soy Candles - I need a flyer to promote my candles and to give information on care of candles.I want this to use the design and colours I already have for my labels and the photo I have attached.I am aiming at a sophisticated market so would like to reflect this in the design.
Should appeal to sophisticated women who enjoy the pleasure of candles - to enhance their enjoyment of life - gives them the 'brume d'orvelle'.
the candles are hand crafted from all natural ingredients, environmentally friendly and with exquisite fragrances

Target Market(s)

sophisticated females

Industry/Entity Type

Promotional

Font styles to use
Script

Colors
cfeae6
ecdaeb

Requirements
Must have
• something expressing 'brume d'orvelle' - the enjoyment of candles
Should not have
• bright colours

```html
<!DOCTYPE html>
<html lang="en">
<head>
<meta charset="utf-8">
<title>Brume d'Orvelle Hand Crafted Candles</title>
<link href="https://fonts.googleapis.com/css2?family=Cinzel:wght@400;500&family=Open+Sans:wght@700&family=Roboto+Condensed:wght@300;400&display=swap" rel="stylesheet">
<style>
  :root {
    --mint-light: #eef7f4;
    --mint: #cfeae6;
    --teal: #7fb3a6;
    --teal-deep: #5b9587;
    --ribbon-top: #94c2b6;
    --ribbon-bottom: #5f9a8c;
    --ribbon-tail: #4f8576;
    --fold: #2f3f3b;
    --text-light: #f4fbf9;
    --panel: #f4f5f5;
    --ink: #262b2a;
  }
  * { box-sizing: border-box; margin: 0; padding: 0; }
  html, body { width: 850px; height: 1200px; overflow: hidden; }
  body {
    position: relative;
    font-family: "Roboto Condensed", sans-serif;
    background:
      radial-gradient(ellipse 70% 45% at 50% 30%, var(--mint-light) 0%, rgba(238,247,244,0) 100%),
      linear-gradient(180deg, #b9dcd4 0%, #d6ece7 30%, #bfded7 55%, var(--teal) 80%, var(--teal-deep) 100%);
  }
  .title-ribbon { position: absolute; left: 30px; top: 86px; width: 790px; height: 112px; }
  .title-ribbon svg { position: absolute; inset: 0; }
  .title-ribbon h1 {
    position: absolute; left: 78px; right: 78px; top: 2px; height: 76px;
    display: flex; align-items: center; justify-content: center;
    font-family: "Cinzel", serif; font-weight: 400; font-size: 58px;
    color: #fff; letter-spacing: 1px; white-space: nowrap;
  }
  .product-photo {
    position: absolute; left: 60px; top: 222px; width: 620px; height: 420px;
    border-radius: 6px;
    background:
      radial-gradient(ellipse 30% 45% at 48% 42%, #2c3450 0%, rgba(44,52,80,0) 100%),
      radial-gradient(ellipse 22% 40% at 22% 55%, #e9e6d6 0%, rgba(233,230,214,0) 100%),
      radial-gradient(ellipse 20% 40% at 72% 50%, #e3dfcf 0%, rgba(227,223,207,0) 100%),
      radial-gradient(ellipse 14% 28% at 88% 62%, #2c3f9a 0%, rgba(44,63,154,0) 100%),
      linear-gradient(180deg, rgba(220,238,234,0) 0%, rgba(200,228,222,.6) 100%);
  }
  .features { position: absolute; left: 30px; top: 648px; width: 790px; display: flex; gap: 8px; }
  .feature { width: 258px; }
  .ribbon { position: relative; height: 56px; }
  .ribbon svg { position: absolute; inset: 0; }
  .ribbon h2 {
    position: absolute; left: 22px; right: 22px; top: 2px; height: 38px;
    display: flex; align-items: center; justify-content: center;
    font-family: "Open Sans", sans-serif; font-weight: 700; font-size: 20px;
    color: #fff; white-space: nowrap;
  }
  .feature ul {
    margin: 12px 0 0 30px; padding-left: 16px;
    color: var(--text-light); font-weight: 300; font-size: 12.3px; line-height: 16px;
  }
  .feature ul li::marker { font-size: 9px; }
  .divider { position: absolute; left: 64px; width: 720px; top: 882px; height: 1px; background: rgba(255,255,255,.8); }
  .contact {
    position: absolute; left: 330px; top: 893px; display: flex; align-items: center; gap: 24px;
    color: var(--text-light); font-weight: 300; font-size: 12.5px; font-style: normal;
  }
  .contact span { display: flex; align-items: center; gap: 14px; }
  .contact svg { flex: none; }
  .care {
    position: absolute; left: 108px; top: 968px; right: 0; bottom: 0;
    background: linear-gradient(90deg, #e9ecec 0%, var(--panel) 30%, #fbfbfb 100%);
  }
  .care-text {
    position: absolute; left: 128px; top: 1186px; width: 206px; height: 700px;
    transform: rotate(-90deg); transform-origin: 0 0;
    color: var(--ink); font-weight: 300; font-size: 11px; line-height: 14.6px;
  }
  .care-text h3 {
    font-weight: 400; font-size: 25px; line-height: 30px; letter-spacing: .3px;
    white-space: nowrap; margin-bottom: 6px;
  }
  .care-text ul { padding-left: 14px; }
  .care-text li::marker { font-size: 8px; }
</style>
</head>
<body>
  <header class="title-ribbon">
    <svg width="790" height="112" viewBox="0 0 790 112" aria-hidden="true">
      <defs>
        <linearGradient id="band" x1="0" y1="0" x2="0" y2="1">
          <stop offset="0" stop-color="#9cc8bc"/><stop offset="1" stop-color="#5f9a8c"/>
        </linearGradient>
      </defs>
      <polygon points="0,26 158,26 158,106 0,106 34,66" fill="#5b8f82"/>
      <polygon points="790,26 632,26 632,106 790,106 756,66" fill="#5b8f82"/>
      <polygon points="78,78 158,78 158,106" fill="var(--fold)"/>
      <polygon points="712,78 632,78 632,106" fill="var(--fold)"/>
      <rect x="78" y="0" width="634" height="78" fill="url(#band)"/>
    </svg>
    <h1>Brume d'Orvelle</h1>
  </header>

  <div class="product-photo" role="img" aria-label="Photograph of four hand crafted soy candles in glass jars with round labels, reflected on a pale surface"></div>

  <section class="features">
    <article class="feature">
      <div class="ribbon">
        <svg width="258" height="56" viewBox="0 0 258 56" aria-hidden="true">
          <polygon points="0,16 60,16 60,54 0,54 14,35" fill="var(--ribbon-tail)"/>
          <polygon points="258,16 198,16 198,54 258,54 244,35" fill="var(--ribbon-tail)"/>
          <polygon points="22,40 60,40 60,54" fill="var(--fold)"/>
          <polygon points="236,40 198,40 198,54" fill="var(--fold)"/>
          <rect x="22" y="2" width="214" height="38" fill="url(#band)"/>
        </svg>
        <h2>BRUME D'ORVELLE</h2>
      </div>
      <ul>
        <li>"an exuberant enjoyment of life" – these candles will fill you with "brume d'orvelle".</li>
        <li>Candles are lovingly hand-poured and use only the finest of ingredients and fragrances</li>
        <li>Hand crafted soy candle creations</li>
        <li>Completely non-toxic</li>
        <li>Exquisite fragrances</li>
        <li>Clean burning</li>
        <li>Environmentally friendly.</li>
      </ul>
    </article>
    <article class="feature">
      <div class="ribbon">
        <svg width="258" height="56" viewBox="0 0 258 56" aria-hidden="true">
          <polygon points="0,16 60,16 60,54 0,54 14,35" fill="var(--ribbon-tail)"/>
          <polygon points="258,16 198,16 198,54 258,54 244,35" fill="var(--ribbon-tail)"/>
          <polygon points="22,40 60,40 60,54" fill="var(--fold)"/>
          <polygon points="236,40 198,40 198,54" fill="var(--fold)"/>
          <rect x="22" y="2" width="214" height="38" fill="url(#band)"/>
        </svg>
        <h2>WHY SOY WAX?</h2>
      </div>
      <ul>
        <li>Soft smooth wax that burns clear – no soot or smoke</li>
        <li>Soy wax candles burn up to 50% longer than traditional paraffin candles</li>
        <li>Made from soya beans, a renewable natural resource that supports and sustains agriculture – it is biodegradable and environmentally friendly</li>
        <li>Soy wax burns cooler than paraffin and disperses the fragrance more fully.</li>
      </ul>
    </article>
    <article class="feature">
      <div class="ribbon">
        <svg width="258" height="56" viewBox="0 0 258 56" aria-hidden="true">
          <polygon points="0,16 60,16 60,54 0,54 14,35" fill="var(--ribbon-tail)"/>
          <polygon points="258,16 198,16 198,54 258,54 244,35" fill="var(--ribbon-tail)"/>
          <polygon points="22,40 60,40 60,54" fill="var(--fold)"/>
          <polygon points="236,40 198,40 198,54" fill="var(--fold)"/>
          <rect x="22" y="2" width="214" height="38" fill="url(#band)"/>
        </svg>
        <h2>REFILLABLE</h2>
      </div>
      <ul>
        <li>I offer a refill service - if you return your containers to me I can refill with the fragrance of your choice</li>
        <li>Or if you have a special container you would like to use for your candle just contact me for a quote.</li>
        <li>I have a wide range of fragrances - please contact me for details.</li>
      </ul>
    </article>
  </section>

  <div class="divider"></div>

  <address class="contact">
    <span>
      <svg width="30" height="20" viewBox="0 0 30 20" aria-hidden="true"><rect x="1" y="1" width="28" height="18" fill="none" stroke="#fff" stroke-width="1.5"/><path d="M1 1 L15 12 L29 1 M1 19 L11 9 M29 19 L19 9" fill="none" stroke="#fff" stroke-width="1.5"/></svg>
      hello@brumedorvelle.co.nz
    </span>
    <span>
      <svg width="24" height="24" viewBox="0 0 24 24" aria-hidden="true"><circle cx="12" cy="12" r="12" fill="#a9d2c8"/><path d="M8 6 q-2 1 -1 4 q2 5 7 8 q3 1 4 -1 l-2 -2 q-1 -1 -2 0 l-1 1 q-3 -2 -4 -4 l1 -1 q1 -1 0 -2 z" fill="#fff"/></svg>
      021-5830614
    </span>
    <span>
      <svg width="24" height="24" viewBox="0 0 24 24" aria-hidden="true"><circle cx="12" cy="12" r="12" fill="#3f6f66"/><g fill="none" stroke="#fff" stroke-width="1.2"><circle cx="12" cy="12" r="7"/><ellipse cx="12" cy="12" rx="3" ry="7"/><path d="M5 12 h14 M6 8.5 h12 M6 15.5 h12"/></g></svg>
      www.brumedorvelle.co.nz
    </span>
  </address>

  <section class="care" aria-label="Care instructions"></section>
  <div class="care-text">
    <h3>CARE INSTRUCTIONS</h3>
    <ul>
      <li>When lighting your candle for the first time, allow the wax to melt all the way to the sides of the container – this creates a 'memory' and avoids 'tunnelling' as the candle burns.</li>
      <li>Always trim the wick to about 6-8mm before re-lighting your candle. This will ensure a long lasting candle, minimise soot and remove any mushrooming of the wick from a previous burn.</li>
      <li>It is preferable to use a candle 'snuffer' to extinguish the flame, or a lid if the candle has one. Alternatively, you can dip the wick into the melted wax and then straighten it. This will stop the wick from smoking and help with relighting.</li>
      <li>All Brume d'Orvelle candles are hand poured, not mass produced – although every effort is made to ensure consistency, every candle may be different.</li>
      <li>Sometimes you may notice darker patches or wet spots - this is not a fault, it is just the natural way the wax has set – it does not affect the candle in anyway.</li>
      <li>The top of the candle may also appear slightly uneven – this is just a sign of natural soy wax being hand poured.</li>
      <li>Do not leave your candle in the sun light as it may turn a yellow colour – again this does not affect the candle in anyway – it just loses its creamy white colour.</li>
      <li>As these candles contain no preservatives or chemicals it is recommended that they should be used within 6 months.</li>
    </ul>
  </div>
</body>
</html>
```